Birchwell Agency Condominium mail merge

We need a marketing proposal letter design to do a mail merge to potential e customers. We included our logo and an example of my miserable attempt to create a template. We are looking for a modern and attractive proposal template. Here is our website https://www.birchwellagency.example to be used for any additional information needed about us and our services.

Target Market(s)

New prospects

Industry/Entity Type

Insurance Agency

Requirements
Must have
• My project must have a modern professional look with merge fields similar to the file uploaded with this project.
Nice to have
• it would like have a condominium and a car icon graphic depicting there is additional discounts for both quotes bundled.
Should not have
• My project should not have any other logos or company name

```html
<!DOCTYPE html>
<html lang="en">
<head>
<meta charset="utf-8">
<title>Birchwell Agency – Letterhead</title>
<link rel="stylesheet" href="https://fonts.googleapis.com/css2?family=Source+Sans+3:wght@400;600;700&family=Arimo:wght@700&display=swap">
<style>
  :root {
    --brand-green: #3db54a;
    --brand-orange: #f58220;
    --ink: #231f20;
    --ink-soft: #444444;
    --paper: #ffffff;
    --backdrop: #e6e6e6;
  }
  * { margin: 0; padding: 0; box-sizing: border-box; }
  html, body {
    width: 1059px; height: 1200px; overflow: hidden;
    background: var(--backdrop);
  }
  .canvas { position: relative; width: 1059px; height: 1200px; }
  .letter {
    position: absolute; left: 104px; top: 0;
    width: 816px; height: 1152px;
    transform: scale(1.0417); transform-origin: 0 0;
    background: var(--paper);
    font-family: "Source Sans 3", sans-serif;
    color: var(--ink);
  }
  .letter-header { position: absolute; left: 0; top: 0; width: 816px; height: 100px; }
  .sender {
    position: absolute; right: 66px; top: 15px;
    text-align: right; color: var(--paper); font-size: 12.5px; line-height: 16px;
  }
  .sender-name { font-weight: 700; font-size: 13px; }
  .sender svg { width: 9px; height: 9px; vertical-align: -1px; margin-left: 2px; }
  .brand {
    position: absolute; left: 70px; top: 72px;
    display: flex; align-items: center; gap: 10px;
  }
  .brand-dot { width: 22px; height: 22px; border-radius: 50%; background: var(--brand-orange); }
  .brand-name { font-size: 30px; font-weight: 700; color: var(--brand-green); letter-spacing: -0.3px; }
  .contact {
    position: absolute; right: 66px; top: 109px;
    text-align: right; font-size: 11px; line-height: 16px; color: var(--ink);
  }
  .contact svg { width: 9px; height: 9px; vertical-align: -1px; margin-left: 3px; }
  .contact .address { margin-top: 4px; }
  .greeting {
    position: absolute; left: 70px; top: 255px;
    font-family: "Arimo", sans-serif; font-weight: 700; font-size: 18px; color: var(--ink-soft);
  }
  .body-copy {
    position: absolute; left: 70px; top: 312px; width: 682px;
    font-size: 15px; line-height: 21px; text-align: justify;
  }
  .body-copy p + p { margin-top: 21px; }
  .signature {
    position: absolute; left: 70px; top: 832px; width: 134px; height: 62px;
    background: linear-gradient(90deg, #eeeeee, #dcdcdc);
    border-radius: 4px;
  }
  .footer-band {
    position: absolute; left: 0; bottom: 0; width: 816px; height: 13px;
    background: var(--brand-green);
  }
</style>
</head>
<body>
<div class="canvas">
  <article class="letter">
    <svg class="letter-header" viewBox="0 0 816 100" aria-hidden="true">
      <path fill="var(--brand-orange)" d="M0,60 C130,14 290,22 430,54 C560,82 720,90 816,68 V84 C720,102 560,94 430,66 C290,36 140,30 0,74 Z"/>
      <path fill="var(--brand-green)" d="M0,0 H816 V64 C720,80 560,72 430,46 C290,18 130,8 0,46 Z"/>
    </svg>

    <div class="sender">
      <div class="sender-name">Marcus Hale</div>
      <div>Agency Principal</div>
      <div>555-014-2290<svg viewBox="0 0 10 10"><path fill="#fff" d="M2,0.5 L3.6,0.5 L4.3,2.8 L3.2,3.8 C3.8,5 4.9,6.2 6.2,6.8 L7.2,5.7 L9.5,6.4 L9.5,8 C9.5,9 8.6,9.6 7.6,9.4 C4,8.7 1.2,5.9 0.6,2.4 C0.4,1.4 1,0.5 2,0.5 Z"/></svg></div>
    </div>

    <div class="brand">
      <span class="brand-dot"></span>
      <span class="brand-name">Birchwell Agency</span>
    </div>

    <div class="contact">
      <div>marcus@birchwellagency.example<svg viewBox="0 0 10 8"><rect width="10" height="8" rx="1" fill="var(--brand-green)"/><path d="M0.5,1 L5,4.5 L9.5,1" stroke="#fff" stroke-width="1" fill="none"/></svg></div>
      <div>www.birchwellagency.example<svg viewBox="0 0 10 10"><circle cx="5" cy="5" r="5" fill="var(--brand-green)"/><path d="M0,5 H10 M5,0 V10 M5,0 C2,3 2,7 5,10 M5,0 C8,3 8,7 5,10" stroke="#fff" stroke-width="0.7" fill="none"/></svg></div>
      <div class="address">2140 Harbor Lane Ste. 310</div>
      <div>Lakemont, FL 30000</div>
    </div>

    <h1 class="greeting">Dear Mr. John,</h1>

    <div class="body-copy">
      <p>Lorem Ipsum is simply dummy text of the printing and typesetting industry. Lorem Ipsum has been the industry's standard dummy text ever since the 1500s, when an unknown printer took a galley of type and scrambled it to make a type specimen book. It has survived not only five centuries, but also the leap into electronic typesetting, remaining essentially unchanged.</p>
      <p>The standard chunk of Lorem Ipsum used since the 1500s is reproduced below for those interested. Sections 1.10.32 and 1.10.33 from "de Finibus Bonorum et Malorum" by Cicero are also reproduced in their exact original form, accompanied by English versions from the 1914 translation by H. Rackham</p>
      <p>Lorem Ipsum is simply dummy text of the printing and typesetting industry. Lorem Ipsum has been the industry's standard dummy text ever since the 1500s, when an unknown printer took a galley of type and scrambled it to make a type specimen book. It has survived not only five centuries, but also the leap into electronic typesetting, remaining essentially unchanged. It was popularised in the</p>
      <p>Lorem Ipsum has been the industry's standard dummy text ever since the 1500s, when an unknown printer took a galley of type and scrambled it to make a type specimen book. It has survived not only five centuries, but also the leap into electronic typesetting, remaining essentially unchanged. It was popularised in the</p>
      <p>Lorem Ipsum is simply dummy text of the printing and typesetting industry. Lorem Ipsum has been the industry's standard dummy text ever since the 1500s, when an unknown printer took a galley of type and scrambled it to make a type specimen book.</p>
    </div>

    <div class="signature" role="img" aria-label="Handwritten signature of the agency principal"></div>

    <div class="footer-band"></div>
  </article>
</div>
</body>
</html>
```